Tallowmoor Letterheads Design

Hello, we have just upgraded this project for a guaranteed payment.

We are currently going through a re-branding exercise internally. Our logo is attached as a PDF file.

We are happy with our logo but would like to investigate how we can best apply the logo to our letterheads and compliment slips.

We are a quality printing company in England. Despite our name we are very professional and offer a personal service.

Our new website is under construction and here is a link to show you how it looks: http://brackenpress.v4ntor.co.uk

The style must be professional and steer away from "tacky" otherwise it makes our company look very low budget and just a bit silly.

We would like to see elements of creativity though, so please, nothing too boring.

I have attached our new logo, there is an option for use on white or black.

Cheers
Tallowmoor Team

Reason: We have increased the deadline due to an internal delay to things, we now have more time before we need anything to be printed.

Industry/Entity Type

Construction

Requirements
Must have
• IMPORTANT! Please do not tweak or change our logo in any way. A few designs show vast changes in the logo, this is not what we require. Please do not change the logo in any way. Thanks
Nice to have
• Classy but approachable. Elements of "quirky" would be nice to see.
Should not have
• A Tacky feel

```html
<!DOCTYPE html>
<html lang="en">
<head>
<meta charset="utf-8">
<title>Tallowmoor Letterhead</title>
<link rel="stylesheet" href="https://fonts.googleapis.com/css2?family=Arimo:wght@400;700&display=swap">
<style>
  :root {
    --ink: #000000;
    --paper: #ffffff;
    --brand-pink: #e8196e;
    --band-light: #b5b5b5;
    --band-dark: #6f6f6f;
    --text: #111111;
  }
  * { box-sizing: border-box; margin: 0; padding: 0; }
  html, body { width: 927px; height: 1200px; overflow: hidden; background: var(--paper); }
  .letterhead {
    position: relative;
    width: 927px;
    height: 1200px;
    overflow: hidden;
    background: var(--paper);
    font-family: "Arimo", Arial, sans-serif;
    color: var(--text);
  }
  .masthead {
    position: absolute;
    left: 0; top: 0;
    width: 927px; height: 235px;
    background: var(--ink);
    color: var(--paper);
  }
  .masthead-band {
    position: absolute;
    left: 0; top: 235px;
    width: 927px; height: 23px;
    background: linear-gradient(to bottom, var(--band-dark), var(--band-light) 55%, #d9d9d9);
  }
  .brand-mark {
    position: absolute;
    left: 122px; top: 52px;
    width: 78px; height: 84px;
    border-radius: 50%;
    background: var(--brand-pink);
  }
  .brand-name {
    position: absolute;
    left: 50px; top: 138px;
    font-size: 39px;
    font-weight: 700;
    letter-spacing: -0.5px;
    line-height: 1;
    color: var(--paper);
  }
  .brand-tagline {
    position: absolute;
    left: 98px; top: 188px;
    font-size: 17px;
    line-height: 1;
    color: var(--paper);
  }
  .masthead-divider {
    position: absolute;
    left: 328px; top: 53px;
    width: 2px; height: 153px;
    background: var(--paper);
  }
  .contact {
    position: absolute;
    left: 373px; top: 67px;
    font-size: 14px;
    line-height: 18.4px;
    font-style: normal;
    color: var(--paper);
  }
  .corner-accent {
    position: absolute;
    left: 812px; top: -60px;
    width: 140px; height: 120px;
  }
  .salutation {
    position: absolute;
    left: 0; top: 315px;
    width: 267px; height: 37px;
    background: var(--ink);
    color: var(--paper);
    font-size: 21px;
    line-height: 37px;
    padding-left: 100px;
  }
  .letter-body {
    position: absolute;
    left: 53px; top: 371px;
    width: 825px;
    font-size: 20px;
    line-height: 26.2px;
    color: var(--text);
  }
  .letter-body p { text-indent: 52px; margin-bottom: 26.2px; }
  .footer-band {
    position: absolute;
    left: 0; top: 1146px;
    width: 927px; height: 19px;
    background: linear-gradient(to bottom, #d9d9d9, var(--band-light) 45%, var(--band-dark));
  }
  .footer-base {
    position: absolute;
    left: 0; top: 1165px;
    width: 927px; height: 35px;
    background: var(--ink);
  }
</style>
</head>
<body>
<div class="letterhead">
  <header class="masthead">
    <div class="brand-mark" role="img" aria-label="Tallowmoor brand symbol area"></div>
    <div class="brand-name">Tallowmoor</div>
    <div class="brand-tagline">Quality Printing</div>
    <div class="masthead-divider"></div>
    <address class="contact">
      18 Mill Lane<br>
      Harrowden-On-The-Hill<br>
      Harrowden<br>
      Surrey<br>
      HR4 2QT<br>
      Phone: 0208 555 0172<br>
      Email:&nbsp; sales@tallowmoor.co.uk
    </address>
  </header>
  <svg class="corner-accent" viewBox="0 0 140 120" role="img" aria-label="Pink decorative corner accent">
    <circle cx="70" cy="60" r="54" fill="var(--brand-pink)" stroke="#000" stroke-width="4"/>
  </svg>
  <div class="masthead-band"></div>

  <div class="salutation">Dear Name Here</div>

  <main class="letter-body">
    <p>Lorem ipsum dolor sit amet, consectetur adipiscing elit. Fusce vel velit mollis, vestibulum libero vel, cursus libero. Ut porta purus sem. Proin congue est quis lectus hendrerit, non viverra sapien fringilla. Mauris varius, turpis vitae rhoncus placerat, augue urna luctus nibh, eu sagittis purus sem at nunc. Nunc sit amet tempor tortor, ut scelerisque massa. Cras eget mi vitae libero pulvinar pellentesque. Vestibulum<br>non luctus risus. Sed venenatis, libero sed vehicula aliquet, urna purus vehicula turpis, sit amet suscipit metus lectus ac nisi. Pellentesque habitant morbi tristique senectus et netus et malesuada fames ac turpis egestas. Curabitur luctus dolor et dapibus lacinia.</p>
    <p>Sed commodo nisi magna, sed ornare massa commodo iaculis. Integer nec interdum tortor. Aliquam aliquam purus odio, nec dapibus orci aliquam eget. Cras et semper nisl. Duis turpis massa, suscipit id accumsan sed, vulputate eu augue. Fusce pulvinar libero id nibh blandit lacinia vitae vitae tellus. Mauris tempus in lorem ut placerat. Nam cursus cursus varius. Donec fringilla malesuada lectus, a rutrum ligula fringilla et. Donec sed metus sed mi mollis fringilla nec et lacus.</p>
    <p>Nam adipiscing velit vel lacus vulputate, non aliquam ante malesuada. Aliquam dapibus, turpis ac porttitor gravida, ligula dui malesuada nisl, at condimentum justo dolor at nulla. In luctus hendrerit auctor. Nam sed mi sit amet felis rutrum dictum quis vel lacus. Suspendisse potenti. Cras velit nunc, luctus quis lacinia tincidunt, elementum quis libero. Sed vehicula ante mi, at venenatis odio semper nec. Phasellus lacinia, ante ut feugiat vestibulum, ligula nibh scelerisque ipsum, eu vulputate turpis tortor faucibus sapien. Morbi sodales iaculis mi. Proin facilisis orci et suscipit tempor. Proin accumsan porta feugiat.</p>
  </main>

  <div class="footer-band"></div>
  <footer class="footer-base"></footer>
</div>
</body>
</html>
```